I need beautiful business cards with Moonpetals and sparrows on then and my tavolink business name is Moonpetals and sparrows.
I sell mini gardens, candles and melts and gift ware....on the other side I would like some thing like...REMEMBER to keep in touch with Moonpetals and sparrows buy a like,comment or just to say hello or tavo link will think you are no longer interested and delete you....you can change the wording to that to make smaller if you would like, and am not sure how to word it....my color theme for my business in purple and green. thank you.

tavo link:Moonpetals and sparrows
mini gardens
candles and melts
gift ware.
email:rosa514@kelvimail.com
phone:0873514062

```html
<!DOCTYPE html>
<html lang="en">
<head>
<meta charset="utf-8">
<title>Moonpetals &amp; Sparrows – Business Cards</title>
<link href="https://fonts.googleapis.com/css2?family=Berkshire+Swash&family=Varela+Round&family=Arimo:ital@0;1&display=swap" rel="stylesheet">
<style>
  :root {
    --backdrop: #ece9e2;
    --card: #f8f6e4;
    --plum: #4a1a5c;
    --plum-soft: #6a3d85;
    --leaf: #8cc63f;
    --lilac: #b7a2d6;
    --ink-plum: #5b2a73;
  }
  * { margin: 0; padding: 0; box-sizing: border-box; }
  html, body {
    width: 1200px; height: 870px; overflow: hidden;
    background: var(--backdrop);
  }
  .canvas { position: relative; width: 1200px; height: 870px; }

  .card {
    position: absolute;
    background: var(--card);
    box-shadow: 0 6px 18px rgba(0,0,0,.18);
    overflow: hidden;
  }

  /* Front card */
  .card--front { left: 75px; top: 40px; width: 410px; height: 650px; }
  .front__emblem { position: absolute; left: 40px; top: 140px; width: 330px; height: 330px; }
  .front__name {
    position: absolute; left: 0; right: 0; top: 492px;
    text-align: center;
    font-family: "Berkshire Swash", cursive; font-weight: 400;
    font-size: 34px; color: var(--leaf);
  }
  .front__rule {
    position: absolute; left: 48px; right: 48px; top: 542px;
    height: 2px; background: var(--lilac);
  }
  .front__tagline {
    position: absolute; left: 0; right: 0; top: 550px;
    text-align: center;
    font-family: "Varela Round", sans-serif;
    font-size: 14px; letter-spacing: .2px; color: var(--lilac);
  }

  /* Back card */
  .card--back { left: 500px; top: 260px; width: 630px; height: 400px; }
  .back__field { position: absolute; left: 0; top: 0; width: 630px; height: 400px; }
  .back__invite {
    position: absolute; right: 22px; top: 52px; width: 260px;
    text-align: right;
    font-family: "Arimo", sans-serif; font-style: italic;
    font-size: 14px; line-height: 1.35; color: var(--lilac);
  }
  .back__contacts {
    position: absolute; right: 22px; top: 134px;
    list-style: none; text-align: right;
    font-family: "Arimo", sans-serif;
    font-size: 15px; color: var(--ink-plum);
  }
  .back__contacts li { margin-bottom: 16px; }
  .back__reminder {
    position: absolute; right: 22px; bottom: 28px;
    text-align: right; color: var(--leaf);
    font-family: "Berkshire Swash", cursive;
  }
  .back__reminder-line { font-size: 16px; }
  .back__reminder-name { font-size: 28px; line-height: 1.1; }
</style>
</head>
<body>
<main class="canvas">

  <section class="card card--front" aria-label="Business card front">
    <svg class="front__emblem" viewBox="0 0 330 330">
      <defs>
        <radialGradient id="emblemGlow" cx="50%" cy="42%" r="60%">
          <stop offset="0%" stop-color="var(--plum-soft)"/>
          <stop offset="100%" stop-color="var(--plum)"/>
        </radialGradient>
      </defs>
      <circle cx="165" cy="165" r="150" fill="url(#emblemGlow)" role="img" aria-label="Dragonfly shape formed from small lilac butterflies"/>
      <circle cx="165" cy="165" r="156" fill="none" stroke="var(--leaf)" stroke-width="7" stroke-linecap="round" stroke-dasharray="0 12"/>
    </svg>
    <h1 class="front__name">Moonpetals &amp; Sparrows</h1>
    <div class="front__rule"></div>
    <p class="front__tagline">mini gardens, candles and melts gift ware.</p>
  </section>

  <section class="card card--back" aria-label="Business card back">
    <svg class="back__field" viewBox="0 0 630 400">
      <defs>
        <radialGradient id="fieldGlow" cx="30%" cy="40%" r="65%">
          <stop offset="0%" stop-color="var(--plum-soft)"/>
          <stop offset="100%" stop-color="var(--plum)"/>
        </radialGradient>
      </defs>
      <circle cx="40" cy="185" r="305" fill="url(#fieldGlow)" role="img" aria-label="Large dragonfly shape formed from lilac butterflies"/>
      <circle cx="40" cy="185" r="311" fill="none" stroke="var(--leaf)" stroke-width="7" stroke-linecap="round" stroke-dasharray="0 12"/>
    </svg>
    <p class="back__invite">Feel free to Like, Comment,<br>&amp; Share on Tavolink.<br>I enjoy hearing from you.</p>
    <ul class="back__contacts">
      <li>tavolink.com/Sparrows.Moonpetals</li>
      <li>email:rosa514@kelvimail.com</li>
      <li>phone:0873514062</li>
    </ul>
    <div class="back__reminder">
      <p class="back__reminder-line">REMEMBER to keep in touch with</p>
      <p class="back__reminder-name">Moonpetals &amp; sparrows</p>
    </div>
  </section>

</main>
</body>
</html>
```